Fast growing Tech company needs redesign of Varnith's end user website!

We need to have our login screen, the dashboard, and the one page of the Varnith site to be redesigned for the end-users. Varnith is a document hosting service for title companies and real estate law firms. This allows the buyers and sellers to view their closing documents after closing along with many other features that help them out during the closing of their property. More information about what we do can be found on our test site https://qpx.482.sampledrafthost.example/. PLEASE NOTE: THE ABOVE SITE IS NOT THE ONE WE NEED REDONE. The above site is our corporate site that explains our service offering and we thought it would be helpful in providing you a better understanding of our service.
The site that we want to have redesigned is for the end user. THE SITE THAT NEEDS TO BE REDONE ARE THE SCREENSHOTS ATTACHED. We will need the login screen, dashboard, and the one page redesigned.
.
We will just need this in HTML and we will then do the rest for the placeholders for logos, data, mapping etc.
Overall, we want a new, fresh, and modern look for the website and we want the login screen, dashboard and one page website to be consistent in design. Again, these are the three screenshots that are attached.
For the winner, we will most likely need to hire you again for more sites because we have other versions.
Thank you and if any questions, please let us know.
Target Market(s)
This site is for buyer and sellers during the closing process of real estate transaction.

```html
<!DOCTYPE html>
<html lang="en">
<head>
<meta charset="utf-8">
<title>Varnith – Closing Dashboard</title>
<link rel="stylesheet" href="https://fonts.googleapis.com/css2?family=Montserrat:wght@300;400;600;700&family=Open+Sans:wght@400;600;700&display=swap">
<style>
:root{
  --blue:#1f78d1;
  --blue-dark:#1660ad;
  --ink:#2b2f38;
  --text:#5d6470;
  --muted:#9aa1ab;
  --line:#d9dee5;
  --band:#f2f3f5;
  --white:#ffffff;
  --green:#3bb54a;
  --red:#d9453b;
  --shadow:0 4px 14px rgba(30,50,80,.12);
}
*{box-sizing:border-box;margin:0;padding:0}
html,body{width:1200px;height:4724px;overflow:hidden}
body{position:relative;background:var(--white);font-family:"Open Sans",Arial,sans-serif;color:var(--text);font-size:14px}
.block{position:absolute;left:0;width:1200px}
.band{background:var(--band)}
.heading{font-family:"Montserrat",Arial,sans-serif;font-size:24px;font-weight:300;color:var(--blue);letter-spacing:.5px;text-transform:uppercase}
.heading b{font-weight:700;color:var(--ink)}
.heading.center{text-align:center}

/* header */
.site-header{top:0;height:48px;display:flex;align-items:center;justify-content:space-between;padding:0 40px 0 104px;background:var(--white)}
.brand{display:flex;align-items:center;gap:8px;font-family:"Montserrat",Arial,sans-serif}
.brand .client{font-weight:700;font-size:15px;color:var(--ink);letter-spacing:.5px}
.brand .by{font-size:10px;color:var(--muted)}
.brand .name{font-weight:700;font-size:14px;color:var(--blue)}
.brand .dot{width:12px;height:12px;border-radius:50%;background:var(--blue)}
.header-tools{display:flex;align-items:center;gap:22px}
.avatar{width:30px;height:30px;border-radius:50%;background:linear-gradient(135deg,#c9a88e,#7a6556)}
.hero{top:48px;height:400px;background:linear-gradient(180deg,#8fa7a0 0%,#6f8a63 40%,#5d7b4d 70%,#8d8f7c 100%)}

/* welcome */
.welcome{top:500px;text-align:center}
.welcome p{width:900px;margin:28px auto 0;font-size:13px;line-height:20px;color:var(--text)}

/* transaction */
.transaction{top:720px;height:780px}
.transaction .heading{margin-top:80px}
.info-card{position:absolute;left:140px;width:360px;background:var(--white);box-shadow:var(--shadow)}
.info-card h3{font-family:"Montserrat",Arial,sans-serif;font-size:13px;font-weight:700;color:var(--blue);text-align:center;padding:12px 0;border-bottom:1px solid var(--line);text-transform:uppercase;letter-spacing:.5px}
.info-card dl{display:grid;grid-template-columns:130px 1fr;row-gap:10px;padding:16px 48px;font-size:13px}
.info-card dt{color:var(--text)}
.info-card dd{color:var(--ink)}
.info-card address{font-style:normal;padding:16px 48px;font-size:13px;line-height:22px;color:var(--ink)}
.map{position:absolute;left:540px;top:152px;width:520px;height:528px;background:linear-gradient(135deg,#9aa39b,#6e7f72 45%,#a7a9a3 75%,#7b8b7a)}

/* milestones */
.milestones{top:1500px;height:740px}
.milestones .heading{margin-top:40px}
.timeline{position:absolute;left:598px;top:100px;width:4px;height:580px;background:var(--line)}
.node{position:absolute;width:14px;height:14px;border-radius:50%;background:var(--line);left:593px}
.node.done{background:var(--blue)}
.node.current{width:24px;height:24px;left:588px;background:var(--white);border:6px solid var(--blue)}
.step{position:absolute;width:240px;height:72px;background:var(--white);box-shadow:var(--shadow);text-align:center;padding-top:16px}
.step.right{left:628px}
.step.left{left:340px}
.step h4{font-family:"Montserrat",Arial,sans-serif;font-size:11px;font-weight:700;color:var(--blue);text-transform:uppercase;letter-spacing:.4px}
.step.pending h4{color:var(--muted);font-weight:600}
.status{display:inline-flex;align-items:center;gap:6px;margin-top:8px;font-size:12px;color:var(--green)}
.status.off{color:var(--muted)}
.tick{width:14px;height:14px;border-radius:2px;background:var(--green);display:inline-flex;align-items:center;justify-content:center}
.status.off .tick{background:var(--muted)}

/* documents & wiring */
.docs{top:2240px;height:480px}
.docs .col-left{position:absolute;left:140px;top:80px;width:440px}
.docs .col-right{position:absolute;left:660px;top:80px;width:400px}
.doc-list{list-style:none;margin-top:24px}
.doc-list li{display:flex;align-items:center;height:56px;font-size:13px;color:var(--ink)}
.pdf{width:16px;height:18px;background:var(--red);border-radius:2px;margin-right:14px}
.doc-list .dl{margin-left:auto;margin-right:52px}
.wire-box{margin-top:24px;width:328px;height:264px;background:var(--white);box-shadow:var(--shadow);padding:24px 28px;font-size:13px;line-height:26px;color:var(--ink)}
.wire-box ul{list-style:none}
.wire-box .download{display:flex;align-items:center;margin-top:6px;font-size:12px;color:var(--text)}
.wire-box .pdf{width:14px;height:16px;margin-right:10px}

/* parties */
.parties{top:2720px;height:560px}
.parties .heading{margin-top:56px}
.party{position:absolute;top:112px;width:288px}
.photo{width:100%;height:268px}
.party h4{margin-top:30px;font-family:"Montserrat",Arial,sans-serif;font-size:13px;font-weight:700;color:var(--blue);text-transform:uppercase}
.party p{font-size:12px;line-height:22px;color:var(--text);display:flex;align-items:center;gap:8px}
.party .role{margin-bottom:2px}

/* moving */
.moving{top:3280px;height:660px}
.moving .heading{position:absolute;top:80px}
.check-card{position:absolute;left:140px;width:440px;height:80px;background:var(--white);box-shadow:var(--shadow);text-align:center;padding-top:20px}
.check-card h4,.wish-card h4{font-family:"Montserrat",Arial,sans-serif;font-size:12px;font-weight:700;color:var(--blue);text-transform:uppercase;letter-spacing:.4px}
.wish-card{position:absolute;left:620px;width:440px;height:72px;background:var(--white);box-shadow:var(--shadow);text-align:center;padding-top:16px}
.wish-card h4{color:var(--muted);font-weight:600}
.wish-add{position:absolute;left:620px;top:336px;width:440px}
.wish-add label{font-family:"Montserrat",Arial,sans-serif;font-size:11px;font-weight:700;color:var(--ink);text-transform:uppercase}
.wish-add .row{display:flex;margin-top:10px;gap:8px}
.wish-add .field{width:360px;height:44px;background:var(--white);border:1px solid var(--line)}
.wish-add .btn{width:72px;height:44px;background:var(--blue);color:var(--white);font-size:12px;font-weight:700;display:flex;align-items:center;justify-content:center}
.cta{position:absolute;top:3968px;left:340px;width:520px;height:52px;background:var(--blue);color:var(--white);font-family:"Montserrat",Arial,sans-serif;font-size:12px;font-weight:700;text-transform:uppercase;display:flex;align-items:center;justify-content:center;letter-spacing:.4px;border-radius:2px}

/* faq */
.faq{top:4080px;height:560px}
.faq-item{position:absolute;left:220px;width:760px;background:var(--white);box-shadow:var(--shadow);padding:16px 80px 16px 40px}
.faq-item h4{font-family:"Montserrat",Arial,sans-serif;font-size:12px;font-weight:700;color:var(--blue);text-transform:uppercase}
.faq-item p{margin-top:12px;font-size:12px;line-height:20px;color:var(--text)}
.faq-item .toggle{position:absolute;right:24px;top:12px;width:24px;height:24px;border-radius:50%;border:1px solid var(--line)}
.faq-item.closed{height:48px}

/* footer */
.site-footer{top:4640px;height:84px;background:#e4e6e9;display:flex;align-items:center;justify-content:center}
</style>
</head>
<body>

<header class="block site-header">
  <div class="brand">
    <span class="client">CLIENT LOGO</span>
    <span class="by">by</span>
    <span class="name">Varnith</span>
    <span class="dot"></span>
  </div>
  <div class="header-tools">
    <svg width="22" height="16" viewBox="0 0 22 16"><rect y="0" width="22" height="2" fill="#1f78d1"/><rect y="7" width="22" height="2" fill="#1f78d1"/><rect y="14" width="22" height="2" fill="#1f78d1"/></svg>
    <div class="avatar" role="img" aria-label="User profile photo"></div>
  </div>
</header>

<div class="block hero" role="img" aria-label="Aerial photo of a suburban neighbourhood with homes and lawns"></div>

<section class="block welcome">
  <h1 class="heading center">Welcome <b>Dana Keller</b></h1>
  <p>Thank you for choosing us for your closing. This page gathers every detail of your purchase in one place, from the status of each step to the documents you will need to review. Check back often as your file moves forward, reach out to any party listed below with questions, and use the moving tools to prepare for your new home before the keys are handed over to you.</p>
</section>

<section class="block band transaction">
  <h2 class="heading center">Transaction <b>Information</b></h2>
  <div class="info-card" style="top:160px">
    <h3>Transaction</h3>
    <dl>
      <dt>File Number:</dt><dd>2018-05667</dd>
      <dt>Buyer:</dt><dd>Dana Keller</dd>
      <dt>Seller:</dt><dd>Owen Pratt</dd>
      <dt>Agent:</dt><dd>Lena Ortiz</dd>
    </dl>
  </div>
  <div class="info-card" style="top:480px">
    <h3>Property Address</h3>
    <address>1480 Harbor Lane<br>Coral Bay, FL 33190</address>
  </div>
  <div class="info-card" style="top:640px">
    <h3>Purchase Details</h3>
    <dl>
      <dt>Purchase Price:</dt><dd>$450,000</dd>
      <dt>Settlement Date:</dt><dd>Tue, Dec 20, 2018</dd>
    </dl>
  </div>
  <div class="map" role="img" aria-label="Aerial map of the property location"></div>
</section>

<section class="block milestones">
  <h2 class="heading center">Closing <b>Milestones</b></h2>
  <div class="timeline"></div>
  <div class="node current" style="top:120px"></div>
  <div class="node done" style="top:233px"></div>
  <div class="node" style="top:337px"></div>
  <div class="node" style="top:433px"></div>
  <div class="node" style="top:529px"></div>
  <div class="node" style="top:633px"></div>

  <div class="step right" style="top:100px"><h4>Transaction Started</h4><span class="status"><span class="tick"><svg width="10" height="8" viewBox="0 0 10 8"><path d="M1 4l3 3 5-6" stroke="#fff" stroke-width="2" fill="none"/></svg></span>Completed</span></div>
  <div class="step left" style="top:200px"><h4>Transaction Started</h4><span class="status"><span class="tick"><svg width="10" height="8" viewBox="0 0 10 8"><path d="M1 4l3 3 5-6" stroke="#fff" stroke-width="2" fill="none"/></svg></span>Completed</span></div>
  <div class="step right pending" style="top:308px"><h4>Delivering Title Report</h4><span class="status off"><span class="tick"></span>Not Completed</span></div>
  <div class="step left pending" style="top:400px"><h4>Title Cleared</h4><span class="status off"><span class="tick"></span>Not Completed</span></div>
  <div class="step right pending" style="top:500px"><h4>Signing Scheduled</h4><span class="status off"><span class="tick"></span>Not Completed</span></div>
  <div class="step left pending" style="top:600px"><h4>Transaction Closed</h4><span class="status off"><span class="tick"></span>Not Completed</span></div>
</section>

<section class="block band docs">
  <div class="col-left">
    <h2 class="heading">Documents <b>You Need to View</b></h2>
    <ul class="doc-list">
      <li><span class="pdf"></span>Closing Paper Work<svg class="dl" width="14" height="14" viewBox="0 0 14 14"><path d="M7 1v8M3 6l4 4 4-4M1 13h12" stroke="#9aa1ab" stroke-width="1.6" fill="none"/></svg></li>
      <li><span class="pdf"></span>Purchase Agreement<svg class="dl" width="14" height="14" viewBox="0 0 14 14"><path d="M7 1v8M3 6l4 4 4-4M1 13h12" stroke="#9aa1ab" stroke-width="1.6" fill="none"/></svg></li>
    </ul>
  </div>
  <div class="col-right">
    <h2 class="heading">Wiring <b>Instructions</b></h2>
    <div class="wire-box">
      <ul>
        <li>Bank Name:</li>
        <li>Bank Address:</li>
        <li>Bank Phone:</li>
        <li>Bank ABA Number:</li>
        <li>Account Number:</li>
        <li>Any Additional Information</li>
      </ul>
      <div class="download"><span class="pdf"></span>Download Wire Instruction Document</div>
    </div>
  </div>
</section>

<section class="block parties">
  <h2 class="heading center">Transaction <b>Parties</b></h2>
  <div class="party" style="left:140px">
    <div class="photo" role="img" aria-label="Portrait photo of the law firm contact" style="background:linear-gradient(160deg,#9ec9cf,#6f8f99)"></div>
    <h4>Nora Delling</h4>
    <p class="role">Real Estate Law Firm</p>
    <p><svg width="12" height="12" viewBox="0 0 12 12"><path d="M2 1l2 0 1 3-1.5 1a7 7 0 003.5 3.5L8 7l3 1v2a1 1 0 01-1 1A9 9 0 011 2a1 1 0 011-1z" fill="#1f78d1"/></svg>(305) 555-0148</p>
    <p><svg width="12" height="10" viewBox="0 0 12 10"><rect x=".5" y=".5" width="11" height="9" fill="none" stroke="#1f78d1"/><path d="M.5 .5l5.5 5 5.5-5" fill="none" stroke="#1f78d1"/></svg>nora@harborlaw.example</p>
  </div>
  <div class="party" style="left:452px">
    <div class="photo" role="img" aria-label="Portrait photo of the real estate agent" style="background:linear-gradient(160deg,#d8d8d6,#8c8e92)"></div>
    <h4>Pete Marlow</h4>
    <p class="role">Real Estate Agent</p>
    <p><svg width="12" height="12" viewBox="0 0 12 12"><path d="M2 1l2 0 1 3-1.5 1a7 7 0 003.5 3.5L8 7l3 1v2a1 1 0 01-1 1A9 9 0 011 2a1 1 0 011-1z" fill="#1f78d1"/></svg>(305) 555-0148</p>
    <p><svg width="12" height="10" viewBox="0 0 12 10"><rect x=".5" y=".5" width="11" height="9" fill="none" stroke="#1f78d1"/><path d="M.5 .5l5.5 5 5.5-5" fill="none" stroke="#1f78d1"/></svg>pete@harborlaw.example</p>
  </div>
  <div class="party" style="left:772px">
    <div class="photo" role="img" aria-label="Portrait photo of the loan officer" style="background:linear-gradient(160deg,#c59a72,#6b4f3a)"></div>
    <h4>Ian Crest</h4>
    <p class="role">Loan Officer</p>
    <p><svg width="12" height="12" viewBox="0 0 12 12"><path d="M2 1l2 0 1 3-1.5 1a7 7 0 003.5 3.5L8 7l3 1v2a1 1 0 01-1 1A9 9 0 011 2a1 1 0 011-1z" fill="#1f78d1"/></svg>(305) 555-0148</p>
    <p><svg width="12" height="10" viewBox="0 0 12 10"><rect x=".5" y=".5" width="11" height="9" fill="none" stroke="#1f78d1"/><path d="M.5 .5l5.5 5 5.5-5" fill="none" stroke="#1f78d1"/></svg>ian@harborlaw.example</p>
  </div>
</section>

<section class="block band moving">
  <h2 class="heading" style="left:140px">Moving <b>Checklist</b></h2>
  <h2 class="heading" style="left:620px">Moving <b>Wishlist</b></h2>

  <div class="check-card" style="top:136px"><h4>Address Change - Post Office</h4><span class="status"><span class="tick"><svg width="10" height="8" viewBox="0 0 10 8"><path d="M1 4l3 3 5-6" stroke="#fff" stroke-width="2" fill="none"/></svg></span>Completed</span></div>
  <div class="check-card" style="top:232px"><h4>Address Change - Bank</h4><span class="status"><span class="tick"><svg width="10" height="8" viewBox="0 0 10 8"><path d="M1 4l3 3 5-6" stroke="#fff" stroke-width="2" fill="none"/></svg></span>Completed</span></div>
  <div class="check-card" style="top:328px"><h4>Address Change - Credit Cards</h4><span class="status"><span class="tick"><svg width="10" height="8" viewBox="0 0 10 8"><path d="M1 4l3 3 5-6" stroke="#fff" stroke-width="2" fill="none"/></svg></span>Completed</span></div>
  <div class="check-card" style="top:424px"><h4>Address Change - Friends/Relatives</h4><span class="status"><span class="tick"><svg width="10" height="8" viewBox="0 0 10 8"><path d="M1 4l3 3 5-6" stroke="#fff" stroke-width="2" fill="none"/></svg></span>Completed</span></div>
  <div class="check-card" style="top:520px"><h4>Address Change - Life Insurance</h4><span class="status"><span class="tick"><svg width="10" height="8" viewBox="0 0 10 8"><path d="M1 4l3 3 5-6" stroke="#fff" stroke-width="2" fill="none"/></svg></span>Completed</span></div>

  <div class="wish-card" style="top:136px"><h4>Need to Call Painting Company</h4><span class="status off"><span class="tick"></span>Not Completed</span></div>
  <div class="wish-card" style="top:232px"><h4>Call Flooring Company</h4><span class="status off"><span class="tick"></span>Not Completed</span></div>
  <div class="wish-add">
    <label>Add Items to Wishlist</label>
    <div class="row"><div class="field"></div><div class="btn">ADD</div></div>
  </div>
</section>

<div class="cta">Click here to change your address/coupon</div>

<section class="block faq">
  <h2 class="heading center" style="margin-top:16px">Frequently <b>Asked Questions</b></h2>
  <div class="faq-item" style="top:80px;height:280px">
    <h4>What should I expect at closing?</h4>
    <p>At the closing table you will review and sign the final loan and transfer papers with the title agent. Bring a valid photo ID and proof that your closing funds have been wired. The agent will explain each page before you sign it, confirm the figures on your settlement statement, and answer any question you have. Once the papers are signed and funds are released, the deed is recorded and the keys to your new home are yours. Most closings take about one hour, so plan your day with a little extra time to spare.</p>
    <span class="toggle"></span>
  </div>
  <div class="faq-item closed" style="top:384px"><h4>What is title insurance?</h4><span class="toggle"></span></div>
  <div class="faq-item closed" style="top:444px"><h4>What is the most important in buying a real estate?</h4><span class="toggle"></span></div>
  <div class="faq-item closed" style="top:504px"><h4>What do I need for loan application</h4><span class="toggle"></span></div>
</section>

<footer class="block site-footer">
  <div class="brand">
    <span class="client">CLIENT LOGO</span>
    <span class="by">by</span>
    <span class="name">Varnith</span>
    <span class="dot"></span>
  </div>
</footer>

</body>
</html>
```